Brantley Water Taxi and Transport

Need to redesign our business cards to relay that we do freight logistics and water taxi service. We also work with gov. agencies doing environmental clean up, oil spill response, remote site construction and work with many of the air taxi and helicopter services on Kodiak Island. Out website is www.brantleywatertaxi-example.com to get a better idea of what we do.

Contact Information for Business Card

I have a previous business card but it just has the logo on the front, and a sunset picture on the back with the contact info. It does not relay what we do and what we can help with. I like a simple straight forward design over a busy one.

Colors
3176b5
0455a3
cfdfed

Requirements
Must have
• logo, email, website, phone number

```html
<!DOCTYPE html>
<html lang="en">
<head>
<meta charset="utf-8">
<title>Brantley Water Taxi &amp; Transport — Business Card</title>
<link rel="stylesheet" href="https://fonts.googleapis.com/css2?family=Lato:wght@400;700;900&display=swap">
<style>
  :root {
    --stage: #3a332f;
    --card: #111112;
    --card-edge: #1c1c1e;
    --brand-blue: #0455a3;
    --accent-blue: #3176b5;
    --pale-blue: #cfdfed;
    --silver: #d9dadc;
    --text-light: #e6e6e6;
    --text-muted: #a9a9ad;
    --divider: #2a2a2e;
  }
  * { box-sizing: border-box; margin: 0; padding: 0; }
  html, body { width: 1200px; height: 844px; overflow: hidden; }
  body {
    background: var(--stage);
    font-family: "Lato", sans-serif;
    display: flex;
    align-items: center;
    justify-content: center;
    gap: 48px;
  }
  .card {
    width: 520px;
    height: 300px;
    background: var(--card);
    border: 1px solid var(--card-edge);
    border-radius: 4px;
    box-shadow: 0 10px 30px rgba(0,0,0,.45);
    position: relative;
    overflow: hidden;
  }

  /* Contact side */
  .card--contact { display: flex; }
  .brand-panel {
    width: 270px;
    flex: none;
    display: flex;
    flex-direction: column;
    justify-content: flex-end;
    padding: 0 16px 42px 30px;
  }
  .brand-art {
    width: 200px;
    height: 100px;
    margin-bottom: 8px;
    border-radius: 4px;
    background: linear-gradient(180deg, #6fb6e6 0%, var(--accent-blue) 55%, var(--brand-blue) 100%);
  }
  .brand-name {
    font-size: 36px;
    font-weight: 700;
    line-height: 1;
    letter-spacing: 1px;
    color: var(--brand-blue);
    text-transform: uppercase;
  }
  .brand-tagline {
    font-size: 17px;
    font-weight: 400;
    color: var(--text-light);
    line-height: 1.25;
    white-space: nowrap;
  }
  .divider {
    width: 1px;
    margin: 30px 0;
    background: var(--divider);
  }
  .details-panel {
    flex: 1;
    padding: 58px 12px 0 22px;
  }
  .person-name {
    font-size: 18px;
    font-weight: 900;
    letter-spacing: .5px;
    text-transform: uppercase;
    color: var(--brand-blue);
    line-height: 1.1;
  }
  .person-role {
    font-size: 12.5px;
    color: var(--text-muted);
    margin-bottom: 16px;
  }
  .contact-list { list-style: none; }
  .contact-item {
    display: flex;
    align-items: center;
    gap: 7px;
    font-size: 12.5px;
    color: var(--text-light);
    margin-bottom: 5px;
    white-space: nowrap;
  }
  .contact-icon { width: 11px; height: 11px; fill: var(--brand-blue); flex: none; }

  /* Front side */
  .card--front {
    display: flex;
    flex-direction: column;
    align-items: center;
    justify-content: center;
  }
  .front-name {
    font-size: 50px;
    font-weight: 700;
    color: var(--silver);
    letter-spacing: 2px;
    line-height: 1;
  }
  .front-tagline {
    font-size: 22px;
    font-weight: 400;
    color: var(--silver);
    margin-top: 4px;
  }
  .service-list {
    list-style: none;
    display: flex;
    flex-wrap: wrap;
    justify-content: center;
    gap: 4px 14px;
    width: 400px;
    margin-top: 22px;
  }
  .service-item {
    font-size: 11px;
    letter-spacing: .6px;
    text-transform: uppercase;
    color: var(--pale-blue);
  }
</style>
</head>
<body>

  <section class="card card--contact">
    <div class="brand-panel">
      <div class="brand-art" role="img" aria-label="Illustration of a boat on blue water beneath mountains and a setting sun"></div>
      <p class="brand-name">Brantley</p>
      <p class="brand-tagline">Water Taxi &amp; Transport</p>
    </div>
    <div class="divider"></div>
    <div class="details-panel">
      <h1 class="person-name">Marcus Hale</h1>
      <p class="person-role">Managing Director</p>
      <ul class="contact-list">
        <li class="contact-item">
          <svg class="contact-icon" viewBox="0 0 24 24" aria-hidden="true"><path d="M6.6 10.8a15 15 0 0 0 6.6 6.6l2.2-2.2c.3-.3.7-.4 1-.2 1.1.4 2.3.6 3.6.6.6 0 1 .4 1 1V20c0 .6-.4 1-1 1A17 17 0 0 1 3 4c0-.6.4-1 1-1h3.5c.6 0 1 .4 1 1 0 1.3.2 2.5.6 3.6.1.3 0 .7-.2 1z"/></svg>
          044-555 010 246
        </li>
        <li class="contact-item">
          <svg class="contact-icon" viewBox="0 0 24 24" aria-hidden="true"><path d="M2 5h20v2l-10 7L2 7z M2 9l10 7 10-7v10H2z"/></svg>
          info@mailbox-example.com
        </li>
        <li class="contact-item">
          <svg class="contact-icon" viewBox="0 0 24 24" aria-hidden="true"><circle cx="12" cy="12" r="10"/></svg>
          www.brantleywatertaxi-example.com
        </li>
      </ul>
    </div>
  </section>

  <section class="card card--front">
    <p class="front-name">BRANTLEY</p>
    <p class="front-tagline">Water Taxi &amp; Transport</p>
    <ul class="service-list">
      <li class="service-item">Freight Logistics</li>
      <li class="service-item">Environmental Clean-Up</li>
      <li class="service-item">Oil Spill Response</li>
      <li class="service-item">Remote Site Construction</li>
    </ul>
  </section>

</body>
</html>
```